Fun A1 2012 family planner using clever typography and block colour

I have been looking for an A1 2012 family planner and I have not been able to find one. Hence I would like help to develop such a planner. I plan to print it on matt paper, portrait orientated. I have attached some reference pictures of our 2011 planner. I like interesting typography, clear clean colours and simple illustration. I need space to write in daily events and need the weeks and days to be clearly delineated from each other. Each day cell needs the date and day in it (please refer to the file uploaded for a visual reference confirming this). Each weekend needs some kind of colour/ typographic delineation. I want a design for a year-at-a-view calendar. I plan to print the planner in Sydney, Australia with plinthworkprints.com.au and probably to sell printed copies online. The terms & conditions of this project are that I will own the design concept 100% and in perpetuity worldwide once payment has been made. (NB. The attached Work File in Word contains a rough layout and all months, days and dates all typed up to make for quicker design.)

Target Market(s)

Reasonably well heeled family of 4. 2 parents. 2 kids. 2 pets.

Industry/Entity Type

Events

Requirements
Must have
• The calendar must be portrait (not landscape orientated), A1 size. It will be printed on matt paper by plinthworkprints.com.au. It must have months running left to right (Jan-Dec) and day/date cells running top to bottom (refer 2011 planner photos in file uploaded). The day/ date cells must be around 3(w)x2(h)cm - big enough to write daily events in. Weekends must be colour/ typographically delineated. 2012 year must be noted as must "A Lanternmoss Inc Project" and web address in fine print bottom left hand left hand corner.
Nice to have
• A Lanternmoss Inc logo in bottom left hand corder (perhaps Nimble Heron like: http://www.artquarry.com/design_submission.aspx?designid=614307). Header/Footer space for customisation (e.g. "Dunmore-Pratt 2012 Planner" or "XYZ Co 2012 Planner".
Should not have
• The calendar should not use photographs or resemble standard or cheesy wall calendars. No watermarks please.

```html
<!DOCTYPE html>
<html lang="en">
<head>
<meta charset="utf-8">
<title>Lanternmoss Inc 2012 Planner</title>
<link rel="stylesheet" href="https://fonts.googleapis.com/css2?family=Didact+Gothic&family=Lobster&display=swap">
<style>
  :root {
    --jan: #f9a535;
    --feb: #ee6d2d;
    --mar: #c8dc2a;
    --apr: #8cc63e;
    --may: #3db449;
    --jun: #13913f;
    --jul: #1aa9e1;
    --aug: #1b75bb;
    --sep: #e8168c;
    --oct: #ee3e36;
    --nov: #f15a2a;
    --dec: #f7941e;
    --corner: #cfe02a;
    --ink: #1c1c1c;
    --date: #707070;
    --paper: #ffffff;
    --paper-edge: #eeeeee;
  }
  * { margin: 0; padding: 0; box-sizing: border-box; }
  html, body { width: 847px; height: 1200px; overflow: hidden; }
  body {
    position: relative;
    background: radial-gradient(ellipse at 50% 45%, var(--paper) 55%, var(--paper-edge) 100%);
    font-family: "Didact Gothic", sans-serif;
  }
  .month-banner { position: absolute; left: 0; top: 0; }
  .month-banner text {
    font-family: "Lobster", cursive;
    font-size: 27px;
    fill: var(--ink);
  }
  .days {
    position: absolute;
    top: 149px;
    list-style: none;
  }
  .days li {
    width: 21px;
    height: 23px;
    margin-bottom: 5.7px;
    padding: 2px 0 0 4px;
    color: var(--date);
    font-size: 11px;
    line-height: 12px;
  }
  .days li i {
    display: block;
    font-style: normal;
    font-size: 5.6px;
    line-height: 7px;
    letter-spacing: 0.1px;
  }
  .days li.we { background: var(--c); color: #fff; }
  .corner { position: absolute; left: 0; top: 974px; }
  .credit {
    position: absolute;
    left: 44px;
    top: 1050px;
    color: #fff;
  }
  .credit .year {
    display: block;
    font-size: 45px;
    line-height: 1;
    letter-spacing: -1px;
  }
  .credit .project {
    display: block;
    margin-top: 1px;
    font-size: 10.5px;
    line-height: 12px;
    letter-spacing: -0.4px;
    white-space: nowrap;
  }
  .credit .web {
    display: block;
    margin-top: 2px;
    font-size: 7px;
    line-height: 8px;
    letter-spacing: 0.1px;
    white-space: nowrap;
  }
</style>
</head>
<body>

<svg class="month-banner" width="847" height="150" viewBox="0 0 847 150" aria-label="Months of 2012">
  <polygon points="28,137 66,61 104,137" fill="var(--jan)"/>
  <polygon points="92.6,61 168.6,61 130.6,137" fill="var(--feb)"/>
  <polygon points="157.2,137 195.2,61 233.2,137" fill="var(--mar)"/>
  <polygon points="221.8,61 297.8,61 259.8,137" fill="var(--apr)"/>
  <polygon points="286.4,137 324.4,61 362.4,137" fill="var(--may)"/>
  <polygon points="351,61 427,61 389,137" fill="var(--jun)"/>
  <polygon points="415.6,137 453.6,61 491.6,137" fill="var(--jul)"/>
  <polygon points="480.2,61 556.2,61 518.2,137" fill="var(--aug)"/>
  <polygon points="544.8,137 582.8,61 620.8,137" fill="var(--sep)"/>
  <polygon points="609.4,61 685.4,61 647.4,137" fill="var(--oct)"/>
  <polygon points="674,137 712,61 750,137" fill="var(--nov)"/>
  <polygon points="738.6,61 814.6,61 776.6,137" fill="var(--dec)"/>
  <g text-anchor="middle">
    <text transform="translate(68,112) rotate(-62)">Jan</text>
    <text transform="translate(133,100) rotate(-62)">Feb</text>
    <text transform="translate(197,112) rotate(-62)">Mar</text>
    <text transform="translate(262,100) rotate(-62)">Apr</text>
    <text transform="translate(326,112) rotate(-62)">May</text>
    <text transform="translate(391,100) rotate(-62)">Jun</text>
    <text transform="translate(456,112) rotate(-62)">Jul</text>
    <text transform="translate(520,100) rotate(-62)">Aug</text>
    <text transform="translate(585,112) rotate(-62)">Sep</text>
    <text transform="translate(650,100) rotate(-62)">Oct</text>
    <text transform="translate(714,112) rotate(-62)">Nov</text>
    <text transform="translate(779,100) rotate(-62)">Dec</text>
  </g>
</svg>

<ol class="days jan" style="--c: var(--jan); left: 55px;">
  <li class="we">01<i>SUN</i></li><li>02<i>MON</i></li><li>03<i>TUE</i></li><li>04<i>WED</i></li><li>05<i>THU</i></li><li>06<i>FRI</i></li><li class="we">07<i>SAT</i></li>
  <li class="we">08<i>SUN</i></li><li>09<i>MON</i></li><li>10<i>TUE</i></li><li>11<i>WED</i></li><li>12<i>THU</i></li><li>13<i>FRI</i></li><li class="we">14<i>SAT</i></li>
  <li class="we">15<i>SUN</i></li><li>16<i>MON</i></li><li>17<i>TUE</i></li><li>18<i>WED</i></li><li>19<i>THU</i></li><li>20<i>FRI</i></li><li class="we">21<i>SAT</i></li>
  <li class="we">22<i>SUN</i></li><li>23<i>MON</i></li><li>24<i>TUE</i></li><li>25<i>WED</i></li><li>26<i>THU</i></li><li>27<i>FRI</i></li><li class="we">28<i>SAT</i></li>
  <li class="we">29<i>SUN</i></li><li>30<i>MON</i></li><li>31<i>TUE</i></li>
</ol>

<ol class="days feb" style="--c: var(--feb); left: 119.6px;">
  <li>01<i>WED</i></li><li>02<i>THU</i></li><li>03<i>FRI</i></li><li class="we">04<i>SAT</i></li><li class="we">05<i>SUN</i></li>
  <li>06<i>MON</i></li><li>07<i>TUE</i></li><li>08<i>WED</i></li><li>09<i>THU</i></li><li>10<i>FRI</i></li><li class="we">11<i>SAT</i></li><li class="we">12<i>SUN</i></li>
  <li>13<i>MON</i></li><li>14<i>TUE</i></li><li>15<i>WED</i></li><li>16<i>THU</i></li><li>17<i>FRI</i></li><li class="we">18<i>SAT</i></li><li class="we">19<i>SUN</i></li>
  <li>20<i>MON</i></li><li>21<i>TUE</i></li><li>22<i>WED</i></li><li>23<i>THU</i></li><li>24<i>FRI</i></li><li class="we">25<i>SAT</i></li><li class="we">26<i>SUN</i></li>
  <li>27<i>MON</i></li><li>28<i>TUE</i></li><li>29<i>WED</i></li>
</ol>

<ol class="days mar" style="--c: var(--mar); left: 184.2px;">
  <li>01<i>THU</i></li><li>02<i>FRI</i></li><li class="we">03<i>SAT</i></li><li class="we">04<i>SUN</i></li>
  <li>05<i>MON</i></li><li>06<i>TUE</i></li><li>07<i>WED</i></li><li>08<i>THU</i></li><li>09<i>FRI</i></li><li class="we">10<i>SAT</i></li><li class="we">11<i>SUN</i></li>
  <li>12<i>MON</i></li><li>13<i>TUE</i></li><li>14<i>WED</i></li><li>15<i>THU</i></li><li>16<i>FRI</i></li><li class="we">17<i>SAT</i></li><li class="we">18<i>SUN</i></li>
  <li>19<i>MON</i></li><li>20<i>TUE</i></li><li>21<i>WED</i></li><li>22<i>THU</i></li><li>23<i>FRI</i></li><li class="we">24<i>SAT</i></li><li class="we">25<i>SUN</i></li>
  <li>26<i>MON</i></li><li>27<i>TUE</i></li><li>28<i>WED</i></li><li>29<i>THU</i></li><li>30<i>FRI</i></li><li class="we">31<i>SAT</i></li>
</ol>

<ol class="days apr" style="--c: var(--apr); left: 248.8px;">
  <li class="we">01<i>SUN</i></li><li>02<i>MON</i></li><li>03<i>TUE</i></li><li>04<i>WED</i></li><li>05<i>THU</i></li><li>06<i>FRI</i></li><li class="we">07<i>SAT</i></li>
  <li class="we">08<i>SUN</i></li><li>09<i>MON</i></li><li>10<i>TUE</i></li><li>11<i>WED</i></li><li>12<i>THU</i></li><li>13<i>FRI</i></li><li class="we">14<i>SAT</i></li>
  <li class="we">15<i>SUN</i></li><li>16<i>MON</i></li><li>17<i>TUE</i></li><li>18<i>WED</i></li><li>19<i>THU</i></li><li>20<i>FRI</i></li><li class="we">21<i>SAT</i></li>
  <li class="we">22<i>SUN</i></li><li>23<i>MON</i></li><li>24<i>TUE</i></li><li>25<i>WED</i></li><li>26<i>THU</i></li><li>27<i>FRI</i></li><li class="we">28<i>SAT</i></li>
  <li class="we">29<i>SUN</i></li><li>30<i>MON</i></li>
</ol>

<ol class="days may" style="--c: var(--may); left: 313.4px;">
  <li>01<i>TUE</i></li><li>02<i>WED</i></li><li>03<i>THU</i></li><li>04<i>FRI</i></li><li class="we">05<i>SAT</i></li><li class="we">06<i>SUN</i></li>
  <li>07<i>MON</i></li><li>08<i>TUE</i></li><li>09<i>WED</i></li><li>10<i>THU</i></li><li>11<i>FRI</i></li><li class="we">12<i>SAT</i></li><li class="we">13<i>SUN</i></li>
  <li>14<i>MON</i></li><li>15<i>TUE</i></li><li>16<i>WED</i></li><li>17<i>THU</i></li><li>18<i>FRI</i></li><li class="we">19<i>SAT</i></li><li class="we">20<i>SUN</i></li>
  <li>21<i>MON</i></li><li>22<i>TUE</i></li><li>23<i>WED</i></li><li>24<i>THU</i></li><li>25<i>FRI</i></li><li class="we">26<i>SAT</i></li><li class="we">27<i>SUN</i></li>
  <li>28<i>MON</i></li><li>29<i>TUE</i></li><li>30<i>WED</i></li><li>31<i>THU</i></li>
</ol>

<ol class="days jun" style="--c: var(--jun); left: 378px;">
  <li>01<i>FRI</i></li><li class="we">02<i>SAT</i></li><li class="we">03<i>SUN</i></li>
  <li>04<i>MON</i></li><li>05<i>TUE</i></li><li>06<i>WED</i></li><li>07<i>THU</i></li><li>08<i>FRI</i></li><li class="we">09<i>SAT</i></li><li class="we">10<i>SUN</i></li>
  <li>11<i>MON</i></li><li>12<i>TUE</i></li><li>13<i>WED</i></li><li>14<i>THU</i></li><li>15<i>FRI</i></li><li class="we">16<i>SAT</i></li><li class="we">17<i>SUN</i></li>
  <li>18<i>MON</i></li><li>19<i>TUE</i></li><li>20<i>WED</i></li><li>21<i>THU</i></li><li>22<i>FRI</i></li><li class="we">23<i>SAT</i></li><li class="we">24<i>SUN</i></li>
  <li>25<i>MON</i></li><li>26<i>TUE</i></li><li>27<i>WED</i></li><li>28<i>THU</i></li><li>29<i>FRI</i></li><li class="we">30<i>SAT</i></li>
</ol>

<ol class="days jul" style="--c: var(--jul); left: 442.6px;">
  <li class="we">01<i>SUN</i></li><li>02<i>MON</i></li><li>03<i>TUE</i></li><li>04<i>WED</i></li><li>05<i>THU</i></li><li>06<i>FRI</i></li><li class="we">07<i>SAT</i></li>
  <li class="we">08<i>SUN</i></li><li>09<i>MON</i></li><li>10<i>TUE</i></li><li>11<i>WED</i></li><li>12<i>THU</i></li><li>13<i>FRI</i></li><li class="we">14<i>SAT</i></li>
  <li class="we">15<i>SUN</i></li><li>16<i>MON</i></li><li>17<i>TUE</i></li><li>18<i>WED</i></li><li>19<i>THU</i></li><li>20<i>FRI</i></li><li class="we">21<i>SAT</i></li>
  <li class="we">22<i>SUN</i></li><li>23<i>MON</i></li><li>24<i>TUE</i></li><li>25<i>WED</i></li><li>26<i>THU</i></li><li>27<i>FRI</i></li><li class="we">28<i>SAT</i></li>
  <li class="we">29<i>SUN</i></li><li>30<i>MON</i></li><li>31<i>TUE</i></li>
</ol>

<ol class="days aug" style="--c: var(--aug); left: 507.2px;">
  <li>01<i>WED</i></li><li>02<i>THU</i></li><li>03<i>FRI</i></li><li class="we">04<i>SAT</i></li><li class="we">05<i>SUN</i></li>
  <li>06<i>MON</i></li><li>07<i>TUE</i></li><li>08<i>WED</i></li><li>09<i>THU</i></li><li>10<i>FRI</i></li><li class="we">11<i>SAT</i></li><li class="we">12<i>SUN</i></li>
  <li>13<i>MON</i></li><li>14<i>TUE</i></li><li>15<i>WED</i></li><li>16<i>THU</i></li><li>17<i>FRI</i></li><li class="we">18<i>SAT</i></li><li class="we">19<i>SUN</i></li>
  <li>20<i>MON</i></li><li>21<i>TUE</i></li><li>22<i>WED</i></li><li>23<i>THU</i></li><li>24<i>FRI</i></li><li class="we">25<i>SAT</i></li><li class="we">26<i>SUN</i></li>
  <li>27<i>MON</i></li><li>28<i>TUE</i></li><li>29<i>WED</i></li><li>30<i>THU</i></li><li>31<i>FRI</i></li>
</ol>

<ol class="days sep" style="--c: var(--sep); left: 571.8px;">
  <li class="we">01<i>SAT</i></li><li class="we">02<i>SUN</i></li>
  <li>03<i>MON</i></li><li>04<i>TUE</i></li><li>05<i>WED</i></li><li>06<i>THU</i></li><li>07<i>FRI</i></li><li class="we">08<i>SAT</i></li><li class="we">09<i>SUN</i></li>
  <li>10<i>MON</i></li><li>11<i>TUE</i></li><li>12<i>WED</i></li><li>13<i>THU</i></li><li>14<i>FRI</i></li><li class="we">15<i>SAT</i></li><li class="we">16<i>SUN</i></li>
  <li>17<i>MON</i></li><li>18<i>TUE</i></li><li>19<i>WED</i></li><li>20<i>THU</i></li><li>21<i>FRI</i></li><li class="we">22<i>SAT</i></li><li class="we">23<i>SUN</i></li>
  <li>24<i>MON</i></li><li>25<i>TUE</i></li><li>26<i>WED</i></li><li>27<i>THU</i></li><li>28<i>FRI</i></li><li class="we">29<i>SAT</i></li><li class="we">30<i>SUN</i></li>
</ol>

<ol class="days oct" style="--c: var(--oct); left: 636.4px;">
  <li>01<i>MON</i></li><li>02<i>TUE</i></li><li>03<i>WED</i></li><li>04<i>THU</i></li><li>05<i>FRI</i></li><li class="we">06<i>SAT</i></li><li class="we">07<i>SUN</i></li>
  <li>08<i>MON</i></li><li>09<i>TUE</i></li><li>10<i>WED</i></li><li>11<i>THU</i></li><li>12<i>FRI</i></li><li class="we">13<i>SAT</i></li><li class="we">14<i>SUN</i></li>
  <li>15<i>MON</i></li><li>16<i>TUE</i></li><li>17<i>WED</i></li><li>18<i>THU</i></li><li>19<i>FRI</i></li><li class="we">20<i>SAT</i></li><li class="we">21<i>SUN</i></li>
  <li>22<i>MON</i></li><li>23<i>TUE</i></li><li>24<i>WED</i></li><li>25<i>THU</i></li><li>26<i>FRI</i></li><li class="we">27<i>SAT</i></li><li class="we">28<i>SUN</i></li>
  <li>29<i>MON</i></li><li>30<i>TUE</i></li><li>31<i>WED</i></li>
</ol>

<ol class="days nov" style="--c: var(--nov); left: 701px;">
  <li>01<i>THU</i></li><li>02<i>FRI</i></li><li class="we">03<i>SAT</i></li><li class="we">04<i>SUN</i></li>
  <li>05<i>MON</i></li><li>06<i>TUE</i></li><li>07<i>WED</i></li><li>08<i>THU</i></li><li>09<i>FRI</i></li><li class="we">10<i>SAT</i></li><li class="we">11<i>SUN</i></li>
  <li>12<i>MON</i></li><li>13<i>TUE</i></li><li>14<i>WED</i></li><li>15<i>THU</i></li><li>16<i>FRI</i></li><li class="we">17<i>SAT</i></li><li class="we">18<i>SUN</i></li>
  <li>19<i>MON</i></li><li>20<i>TUE</i></li><li>21<i>WED</i></li><li>22<i>THU</i></li><li>23<i>FRI</i></li><li class="we">24<i>SAT</i></li><li class="we">25<i>SUN</i></li>
  <li>26<i>MON</i></li><li>27<i>TUE</i></li><li>28<i>WED</i></li><li>29<i>THU</i></li><li>30<i>FRI</i></li>
</ol>

<ol class="days dec" style="--c: var(--dec); left: 765.6px;">
  <li class="we">01<i>SAT</i></li><li class="we">02<i>SUN</i></li>
  <li>03<i>MON</i></li><li>04<i>TUE</i></li><li>05<i>WED</i></li><li>06<i>THU</i></li><li>07<i>FRI</i></li><li class="we">08<i>SAT</i></li><li class="we">09<i>SUN</i></li>
  <li>10<i>MON</i></li><li>11<i>TUE</i></li><li>12<i>WED</i></li><li>13<i>THU</i></li><li>14<i>FRI</i></li><li class="we">15<i>SAT</i></li><li class="we">16<i>SUN</i></li>
  <li>17<i>MON</i></li><li>18<i>TUE</i></li><li>19<i>WED</i></li><li>20<i>THU</i></li><li>21<i>FRI</i></li><li class="we">22<i>SAT</i></li><li class="we">23<i>SUN</i></li>
  <li>24<i>MON</i></li><li>25<i>TUE</i></li><li>26<i>WED</i></li><li>27<i>THU</i></li><li>28<i>FRI</i></li><li class="we">29<i>SAT</i></li><li class="we">30<i>SUN</i></li>
  <li>31<i>MON</i></li>
</ol>

<svg class="corner" width="235" height="226" viewBox="0 0 235 226" aria-hidden="true">
  <polygon points="0,0 233,102 0,212" fill="var(--corner)"/>
</svg>
<div class="credit">
  <span class="year">2012</span>
  <span class="project">A Lanternmoss Inc Project</span>
  <span class="web">www.lanternmoss.com.au</span>
</div>

</body>
</html>
```